Website template and forms
Velvet lantern
Website template and forms  - Financial Services
Creative Brief
Financial Services
http://www.velvet-lantern.co.uk
Velvet Lantern works as an intermediary between clients who are looking into products such as life insurance and the IFA and Brokerage community who can assist them.
We have teamed up with some of the countries largest survey companies and respond directly to customers who have suggested they may be interested in learning more.
General knowledge about life insurance and how it operates is limited within what the industry terms “the insurance gap” and our aim is to ensure our customers understand the products they are interested in and they feel the products are suitable for them.
Whilst we do not provide or offer advice at any time, we spend time talking with customers about their need for cover. We find a lot of our customers have made the decision that they need to have cover in place but have yet to think about how much cover they require and over what time period. This can cause difficulties when calling into brokerages directly or indeed when using comparison sites, where you are asked direct questions and are not always equipped with the answers. This can then be a frustrating process for all involved.
We have essentially two sets of customers, the customers who respond to surveys and whom we then call and assist and also the IFA/Brokerages with whom we place our leads.
We will only transfer a client to a brokerage when they have a good understanding of what they are looking for, often we can outline the areas to think about and arrange to call the client back. This works for everyone concerned as the buyer knows what they are looking for and understands what the product does and doesn’t do and also ensures that the commercial side of our business, which is lead provision maintains its reputation.
We have long term relationships with our clients and companies have chosen us as their sole partner for Life insurance transfers. We work continually on our approach and service so that brokerages receive those customers whom they feel they can benefit; taking daily feedback on every lead we supply to ensure standards are high.
Each brokerage has its own set of criteria and parameters for customers, for example IFA companies who like to advise clients need the customers to have enough time to spare to complete a fact find and have their needs assessed. Brokerages offer a quick and comprehensive service often finding customers much more competitive products than they would otherwise have access to.
Like : Exisiting logo. Dislikes: Flash, moving images, unindexable content
Colorful
Humorous
yellow
what ever works
Arial, Verdana, Trebuchet MS, Times New Roman, Century Gothic, Georgia
left side
please email derek@velvet-lantern.co.uk for the full design brief. We also need some auto email forms creating as part of the project. Please inform me if you cannot do this.

```html
<!DOCTYPE html>
<html lang="en">
<head>
<meta charset="utf-8">
<title>Velvet Lantern – Life Insurance Quote Portal</title>
<link rel="stylesheet" href="https://fonts.googleapis.com/css2?family=PT+Sans:wght@400;700&family=Open+Sans:wght@400;600;700&display=swap">
<style>
:root{
  --nav-top:#4a4d52;
  --nav-bottom:#26282b;
  --nav-pill:#2f6db3;
  --hero-deep:#163e72;
  --hero-mid:#2a62a3;
  --hero-light:#4b86c4;
  --gold:#f6b718;
  --gold-dark:#d99500;
  --gold-light:#ffd65a;
  --tick-box:#3a3a3a;
  --page:#ffffff;
  --box-border:#d9dbde;
  --box-bg:#fbfbfb;
  --text:#5d6165;
  --heading:#2b4f78;
  --heading-dark:#3a3d40;
  --icon:#8e949a;
  --footer-top:#3a352f;
  --footer-bottom:#1d1a17;
  --form-bg:#f4f5f6;
  --form-border:#9aa3ad;
  --form-head:#d8dde3;
}
*{box-sizing:border-box;margin:0;padding:0}
html,body{width:1200px;height:1091px;overflow:hidden;background:var(--page)}
body{position:relative;font-family:"Open Sans",Arial,sans-serif;color:var(--text)}

/* navigation */
.site-nav{position:absolute;left:0;top:0;width:1200px;height:56px;background:linear-gradient(var(--nav-top),var(--nav-bottom))}
.nav-links{position:absolute;left:30px;top:13px;display:flex;gap:8px;list-style:none}
.nav-links li{font:700 14px "PT Sans",Arial,sans-serif;color:#e8eaec;padding:6px 14px;border-radius:4px}
.nav-links li.is-current{background:var(--nav-pill);box-shadow:inset 0 1px 0 rgba(255,255,255,.3)}
.search{position:absolute;right:28px;top:16px;display:flex;align-items:center;gap:10px}
.search-field{width:200px;height:24px;background:#f1f2f3;border-radius:3px;font-size:12px;color:#a4a8ac;padding:4px 8px}
.search-label{font:700 13px "PT Sans",Arial,sans-serif;color:#e8eaec}

/* hero */
.hero{position:absolute;left:0;top:56px;width:1200px;height:446px;background:radial-gradient(ellipse at 55% 30%,var(--hero-light),var(--hero-mid) 40%,var(--hero-deep) 100%);overflow:hidden}
.hero-art{position:absolute;left:30px;top:10px;width:190px;height:420px;border-radius:40% 40% 20% 20%;background:radial-gradient(circle at 50% 35%,#4a9ad8,#1e5d9c 60%,rgba(30,93,156,0) 80%)}
.brand{position:absolute;left:232px;top:140px;display:flex;align-items:center;gap:12px}
.brand-mark{width:20px;height:20px;border-radius:50%;background:var(--gold)}
.brand-name{font:700 50px/1.05 "PT Sans",Arial,sans-serif;color:#ffffff;letter-spacing:1px}

.quote-form{position:absolute;left:578px;top:120px;width:282px;height:252px;background:var(--form-bg);border:1px solid var(--form-border);box-shadow:0 6px 16px rgba(0,0,0,.35);font-size:9px;color:#33373b}
.quote-form h2{font:700 11px "Open Sans",Arial,sans-serif;background:var(--form-head);padding:5px 10px;border-bottom:1px solid var(--form-border)}
.form-row{display:flex;align-items:center;height:34px;padding:0 8px}
.form-row label{width:138px;text-align:right;padding-right:8px;font-weight:600;line-height:1.25}
.form-control{width:105px;height:16px;background:#fff;border:1px solid #aab1b8;font-size:9px;padding:1px 4px;color:#555}
.form-control.short{width:40px}
.form-note{margin-left:6px;font-size:9px;color:#777}
.radio{display:inline-flex;align-items:center;gap:3px;margin-right:10px}
.radio::before{content:"";width:9px;height:9px;border:1px solid #888;border-radius:50%;background:#fff}

.product-tabs{position:absolute;left:868px;top:68px;list-style:none}
.product-tab{position:relative;width:272px;height:60px;margin-bottom:30px;background:linear-gradient(var(--gold-light),var(--gold) 55%,var(--gold-dark));border-radius:6px 0 0 6px;box-shadow:0 3px 8px rgba(0,0,0,.35);padding:8px 0 0 14px}
.product-tab strong{display:block;font:400 22px "PT Sans",Arial,sans-serif;color:#2d2a22;line-height:1.05}
.product-tab span{font-size:11px;color:#5a4410}
.product-tab.compact strong{font-size:18px}
.product-tab.compact span{font-size:15px;color:#2d2a22}
.tick-box{position:absolute;right:6px;top:8px;width:44px;height:44px;background:var(--tick-box);border-radius:3px;display:flex;align-items:center;justify-content:center}

/* content */
.why-pick{position:absolute;left:40px;top:538px;display:flex;align-items:center;gap:14px}
.question-badge{width:58px;height:58px;background:var(--gold);border-radius:4px;display:flex;align-items:center;justify-content:center;font:700 40px "PT Sans",Arial,sans-serif;color:#fff}
.why-pick h2{font:400 22px "PT Sans",Arial,sans-serif;color:var(--heading-dark);line-height:1.1}
.why-pick h2 b{display:block;font-size:30px}
.portal-title{position:absolute;left:525px;top:542px;font:700 42px "PT Sans",Arial,sans-serif;color:var(--heading)}
.divider{position:absolute;left:30px;top:610px;width:1140px;height:2px;background:var(--box-border)}

.feature{position:absolute;width:550px;height:158px;background:var(--box-bg);border:1px solid var(--box-border);border-radius:4px;box-shadow:0 1px 3px rgba(0,0,0,.08)}
.feature .icon{position:absolute;left:22px;top:24px;width:110px;height:110px}
.feature p{position:absolute;left:148px;top:22px;width:375px;font-size:13px;line-height:1.5}
.read-more{position:absolute;right:16px;bottom:12px;background:linear-gradient(var(--gold-light),var(--gold));border:1px solid var(--gold-dark);border-radius:3px;padding:3px 12px;font-size:12px;font-weight:600;color:#4a3708}
.feature-a{left:30px;top:625px}
.feature-b{left:620px;top:625px}
.feature-c{left:30px;top:800px}
.feature-d{left:620px;top:800px}

/* footer */
.site-footer{position:absolute;left:0;top:995px;width:1200px;height:96px;background:linear-gradient(var(--footer-top),var(--footer-bottom))}
.newsletter{position:absolute;left:350px;top:20px;display:flex;gap:12px}
.newsletter-field{width:300px;height:26px;background:#6b655d;border:1px solid #857e75;font-size:11px;color:#cfc8be;padding:5px 8px;letter-spacing:.5px}
.subscribe{height:26px;padding:5px 14px;background:linear-gradient(var(--gold-light),var(--gold));border-radius:2px;font-size:11px;font-weight:700;color:#3e2f07}
.copyright{position:absolute;left:0;top:64px;width:1200px;text-align:center;font-size:11px;color:#d9d3ca}
.social{position:absolute;left:975px;top:975px;display:flex;gap:14px}
.social span{width:62px;height:62px;border-radius:10px;background:linear-gradient(#6cc4f0,#2b88c8);box-shadow:0 4px 10px rgba(0,0,0,.4)}
.social span:first-child{transform:rotate(-10deg)}
.social span:last-child{transform:rotate(8deg) translateY(-14px);background:linear-gradient(#5b8fd6,#2e5ea8)}
</style>
</head>
<body>

<nav class="site-nav">
  <ul class="nav-links">
    <li class="is-current">Home</li>
    <li>About Us</li>
    <li>Leave a comment</li>
    <li>Contact Us</li>
  </ul>
  <div class="search"><div class="search-field">Search here...</div><span class="search-label">Search</span></div>
</nav>

<header class="hero">
  <div class="hero-art" role="img" aria-label="Illustrated lantern character mascot holding a coin"></div>
  <div class="brand"><span class="brand-mark"></span><span class="brand-name">Velvet<br>Lantern</span></div>

  <form class="quote-form">
    <h2>Life Insurance Information</h2>
    <div class="form-row"><label>What type of cover are you looking for?</label><span class="form-control">Select</span></div>
    <div class="form-row"><label>How much cover do you need?</label><span class="form-control">£</span></div>
    <div class="form-row"><label>Length of term?</label><span class="form-control short">Select</span><span class="form-note">(Years)</span></div>
    <div class="form-row"><label>Are you a smoker?</label><span class="radio">Yes</span><span class="radio">No</span></div>
    <div class="form-row"><label>Premium type?</label><span class="form-control">Select</span></div>
    <div class="form-row"><label>Level or Decreasing Cover?</label><span class="form-control">Select</span></div>
  </form>

  <ul class="product-tabs">
    <li class="product-tab"><strong>Life Insurance</strong><span>know more about it</span>
      <span class="tick-box"><svg width="26" height="26" viewBox="0 0 26 26"><path d="M4 14l6 6L22 5" fill="none" stroke="#fff" stroke-width="4"/></svg></span></li>
    <li class="product-tab"><strong>Broker Area</strong><span>know more about it</span>
      <span class="tick-box"><svg width="26" height="26" viewBox="0 0 26 26"><path d="M4 14l6 6L22 5" fill="none" stroke="#fff" stroke-width="4"/></svg></span></li>
    <li class="product-tab"><strong>Home Insurance</strong><span>know more about it</span>
      <span class="tick-box"><svg width="26" height="26" viewBox="0 0 26 26"><path d="M4 14l6 6L22 5" fill="none" stroke="#fff" stroke-width="4"/></svg></span></li>
    <li class="product-tab compact"><strong>Over 50 Life Insurance</strong><span>no Medicals</span>
      <span class="tick-box"><svg width="26" height="26" viewBox="0 0 26 26"><path d="M4 14l6 6L22 5" fill="none" stroke="#fff" stroke-width="4"/></svg></span></li>
  </ul>
</header>

<main>
  <div class="why-pick"><span class="question-badge">?</span><h2>Why Pick <b>VelvetLantern</b></h2></div>
  <h1 class="portal-title">Life Insurance Quote Portal</h1>
  <div class="divider"></div>

  <section class="feature feature-a">
    <svg class="icon" viewBox="0 0 110 110" fill="var(--icon)">
      <circle cx="35" cy="22" r="7"/><rect x="28" y="31" width="14" height="28" rx="4"/>
      <circle cx="70" cy="40" r="7"/><rect x="63" y="49" width="14" height="28" rx="4"/>
      <circle cx="30" cy="68" r="6"/><rect x="24" y="76" width="12" height="24" rx="4"/>
    </svg>
    <p>Velvet Lantern works as an intermediary between clients who are looking into products such as life insurance and the IFA and Brokerage community who can assist them.</p>
    <span class="read-more">Read More</span>
  </section>

  <section class="feature feature-b">
    <svg class="icon" viewBox="0 0 110 110" fill="none" stroke="var(--icon)" stroke-width="3">
      <circle cx="55" cy="55" r="38"/><ellipse cx="55" cy="55" rx="16" ry="38"/><path d="M17 55h76M24 36h62M24 74h62"/>
    </svg>
    <p>We have teamed up with some of the countries largest survey companies and respond directly to customers who have suggested they may be interested in learning more.</p>
    <span class="read-more">Read More</span>
  </section>

  <section class="feature feature-c">
    <svg class="icon" viewBox="0 0 110 110" fill="none" stroke="var(--icon)" stroke-width="4">
      <path d="M20 30l7 7 13-14M20 60l7 7 13-14M20 90l7 7 13-14"/><path d="M52 32h40M52 62h40M52 92h40" stroke-width="3"/>
    </svg>
    <p>We have essentially two sets of customers, the customers who respond to surveys and whom we then call and assist and also the IFA/Brokerages with whom we place our leads.</p>
    <span class="read-more">Read More</span>
  </section>

  <section class="feature feature-d">
    <svg class="icon" viewBox="0 0 110 110" fill="var(--icon)">
      <circle cx="58" cy="22" r="9"/><path d="M46 40h20l-8 52h10v8H38v-8h9l6-44h-7z"/>
    </svg>
    <p>and much more...</p>
    <span class="read-more">Read More</span>
  </section>
</main>

<footer class="site-footer">
  <div class="newsletter"><div class="newsletter-field">SUBSCRIBE TO OUR NEWSLETTER</div><span class="subscribe">SUBSCRIBE</span></div>
  <p class="copyright">Copyright © 2011 Velvet Lantern. Terms &amp; Conditions</p>
</footer>
<div class="social" aria-hidden="true"><span></span><span></span></div>

</body>
</html>
```